Wordpress Design Project - New Website for Catering Company

Thistle Private Catering is looking for a new and improved website to sell its Private Catering Service to London and S.E based businesses and private clients. Our current website www.thistlebrandex.co.uk details our offerings, but it is rather plain currently and we would like something much more image focused. Attached is also our new logo.

We would like to include lots of images of lovely food (canapés, dinners, artisan breads, yummy cheeses, fresh ingredients, cakes, brownies etc) to show we are high-end chefs that produce delicious, fresh and seasonal food. We have some stock images that we have taken and own, but we are also interested in using stock photography from elsewhere. Some other catering and food websites that we like are….

www.marlowandfern.example (we like the use of images on this site and the simple layout and navigation)
www.bluegatecatering.example (we like the use of images to illustrate the services offered)
http://www.honeyandthymefood.example/index.php?option=com_content&view=frontpage&Itemid=1 (again an image based site that we like. We also want to incorporate a 'seasonal recipe' section that we can update regularly and easily
http://minas-larder.example/ (we also quite like the idea of rotating images on the home page, like this site. We also like the idea of a 'less is more' homepage, that isn't overloaded with info
http://www.thecornerpantry.example/ (we like the simple homepage on this one)

We would like the menu to run as follows…..

1) Homepage (image lead, basic info about us, quick link to seasonal recipe)

2) Services
2.1 Canapes
2.2 Working Lunches
2.3 Dinner Parties
2.4 Fork buffets
2.5 Food for Children
2.6 Celebrations (Wedding / Christenings)
2.7 Freezer Filling / Drop off Dinners
2.8 Hampers and Food Gifts
2.9 Wine Matching & Drinks

3) Staff

4) Menus
4.1 Spring/Summer Canape Menu
4.2 Autumn/Winter Canape Menu
4.3 Spring/Summer Buffet Menu
4.4 Autumn/Winter Buffet Menu
4.5 Spring/Summer Dinner Party Menu
4.6 Autumn/Winter Dinner Party Menu
4.7 Wine List

5) Seasonal Recipe

6) Testimonials & Clients

7) About us & Contact Details

We would also like to be able to update the seasonal recipe page easily and potentially also turn this in to a mail shot which we can send to clients - we'd like this integrated in to the CMS.

We currently have a twitter account - thistle cooks and a Facebook page (Thistle Private Catering) which we would also like to integrate in to the website.

We would like a word press or joomla site which we are able to manage easily.
Updates

Project Deadline Extended
Reason: I think the sites that have come through are a good start, but we are looking for something a little more high-end I think - particularly with regards to the food images used on the site.

Project Deadline Extended

Target Market(s)

London based companies wanting high-end catering e.g marketing agencies, lawyers, financial industries. Also private clients wanting parties

Industry/Entity Type

Catering

Requirements
Must have
• Link to our twitter and Facebook account.

Seasonal recipe page that is easy for us to update (we aren't technical at all!)

```html
<!DOCTYPE html>
<html lang="en">
<head>
<meta charset="utf-8">
<title>Thistle Private Catering</title>
<link rel="stylesheet" href="https://fonts.googleapis.com/css2?family=Ubuntu:ital,wght@0,400;0,500;1,400&family=Ubuntu+Condensed&display=swap">
<style>
  :root {
    --leaf: #a3c98a;
    --page: #ffffff;
    --plum: #5a2948;
    --plum-dark: #3f1c33;
    --green-head: #6b9a3c;
    --ink: #2b2b2b;
    --rule: #cfcfcf;
    --social-blue: #3b5998;
  }
  * { margin: 0; padding: 0; box-sizing: border-box; }
  html, body { width: 919px; height: 1200px; overflow: hidden; }
  body { background: var(--leaf); font-family: "Ubuntu", sans-serif; color: var(--ink); position: relative; }
  .page { position: absolute; left: 20px; top: 0; width: 879px; height: 1200px; background: var(--page); }
  .abs { position: absolute; }

  .nav { position: absolute; display: flex; align-items: center; white-space: nowrap; }
  .nav a { font-family: "Ubuntu Condensed", "Arial Narrow", sans-serif; font-size: 13.5px; color: #111; text-decoration: none; line-height: 28px; letter-spacing: -0.2px; }
  .nav-left { left: 55px; top: 81px; gap: 22px; }
  .nav-right { right: 50px; top: 80px; gap: 18px; }
  .nav .current { background: var(--plum); color: #fff; border-radius: 3px; width: 62px; text-align: center; }

  .brand { left: 300px; top: 58px; width: 300px; text-align: center; font-family: "Ubuntu", sans-serif; font-weight: 500; font-size: 24px; line-height: 30px; color: var(--plum); white-space: nowrap; }
  .brand-mark { left: 438px; top: 24px; width: 24px; height: 24px; border-radius: 50%; background: var(--leaf); }

  .social { top: 28px; width: 23px; height: 23px; border-radius: 4px; background: #8a8a8a; }

  .hero { left: 49px; top: 126px; width: 821px; height: 349px; border-radius: 6px;
    background: linear-gradient(120deg, #6c9a3a 0%, #e8e4d8 35%, #f2efe8 50%, #c98a4a 70%, #8a3a2a 100%); }
  .hero-shadow { left: 140px; top: 472px; width: 640px; height: 36px; border-radius: 50%;
    background: radial-gradient(ellipse at center top, rgba(0,0,0,.55) 0%, rgba(0,0,0,0) 70%); }

  .slider-dot { top: 516px; width: 12px; height: 12px; border-radius: 50%; background: radial-gradient(circle at 40% 35%, #f2f2f2, #bdbdbd); }
  .slider-dot.active { background: radial-gradient(circle at 40% 35%, #b6d89a, #5f8f3a); }

  h2.section-title { position: absolute; font-family: "Ubuntu", sans-serif; font-style: italic; font-weight: 400; color: var(--green-head); font-size: 18px; line-height: 22px; white-space: nowrap; }

  .photo { position: absolute; border-radius: 5px; }
  .intro-text { left: 308px; top: 612px; width: 300px; font-size: 11.1px; line-height: 17.6px; color: var(--ink); }

  .btn { display: block; background: var(--plum); color: #fff; font-family: "Ubuntu", sans-serif; font-size: 13px; line-height: 23px; height: 23px; width: 55px; text-align: center; border-radius: 3px; text-decoration: none; }

  .rule { left: 49px; top: 832px; width: 560px; height: 2px; background: var(--rule); }

  .column { position: absolute; width: 256px; }
  .column-text { font-family: Arial, sans-serif; font-size: 11.4px; line-height: 13.4px; color: #111; letter-spacing: -0.1px; }
  .column-text a { color: #0000ee; }
  .column .btn { margin-top: 12px; }

  .sidebar-box { left: 658px; top: 567px; width: 212px; height: 351px; background: var(--plum); border-radius: 4px; }
  .sidebar-title { font-style: italic; color: #fff; font-size: 15px; }
  .thumb { position: absolute; width: 76px; height: 76px; border-radius: 4px; border: 2px solid #fff; box-shadow: 1px 2px 3px rgba(0,0,0,.5); }
  .see-all { left: 685px; top: 880px; width: 77px; height: 22px; background: var(--plum-dark); color: #fff; font-family: Arial, sans-serif; font-weight: bold; font-size: 11px; line-height: 22px; padding-left: 11px; border-radius: 3px; }

  .fb-avatar { left: 667px; top: 943px; width: 36px; height: 36px; background: linear-gradient(135deg, #6a4a3a, #c9a07a); }
  .fb-name { left: 713px; top: 942px; font-family: Arial, sans-serif; font-weight: bold; font-size: 13px; color: var(--social-blue); white-space: nowrap; }
  .fb-like { left: 713px; top: 963px; width: 43px; height: 20px; border: 1px solid #c4cde0; border-radius: 3px; background: #eceef5; font-family: Arial, sans-serif; font-size: 10px; line-height: 18px; color: var(--social-blue); text-align: center; }
  .fb-count { left: 768px; top: 967px; font-family: Arial, sans-serif; font-size: 10px; color: #333; }

  .video-head { left: 656px; top: 1004px; width: 212px; height: 37px; background: var(--plum); border-radius: 4px 4px 0 0; padding: 10px 0 0 16px; }
  .video { left: 656px; top: 1041px; width: 212px; height: 159px; background: linear-gradient(160deg, #8fb45a 0%, #d9c06a 45%, #b9852f 100%); }
</style>
</head>
<body>
<div class="page"></div>

<nav class="nav nav-left">
  <a class="current" href="#">Home</a>
  <a href="#">About</a>
  <a href="#">Menus</a>
  <a href="#">Services</a>
</nav>
<nav class="nav nav-right">
  <a href="#">Staff</a>
  <a href="#">Seasonal Recipe</a>
  <a href="#">Testimonials</a>
  <a href="#">Contact</a>
</nav>

<div class="abs brand-mark"></div>
<div class="abs brand">Thistle Private Catering</div>

<div class="abs social" style="left:764px;" aria-label="Social link"></div>
<div class="abs social" style="left:791px;" aria-label="Social link"></div>
<div class="abs social" style="left:818px;" aria-label="Social link"></div>
<div class="abs social" style="left:845px;" aria-label="Feed link"></div>

<div class="abs hero" role="img" aria-label="Photograph of fresh ingredients: vegetables, breads, dairy and cured meats"></div>
<div class="abs hero-shadow"></div>

<svg class="abs" style="left:354px;top:513px;" width="18" height="18" viewBox="0 0 18 18" aria-label="Previous slide">
  <circle cx="9" cy="9" r="9" fill="#111"/><path d="M10.5 5 L6.5 9 L10.5 13" stroke="#fff" stroke-width="2" fill="none"/>
</svg>
<div class="abs slider-dot active" style="left:383px;"></div>
<div class="abs slider-dot" style="left:403px;"></div>
<div class="abs slider-dot" style="left:423px;"></div>
<div class="abs slider-dot" style="left:442px;"></div>
<div class="abs slider-dot" style="left:462px;"></div>
<div class="abs slider-dot" style="left:482px;"></div>
<div class="abs slider-dot" style="left:502px;"></div>
<div class="abs slider-dot" style="left:522px;"></div>
<svg class="abs" style="left:546px;top:513px;" width="18" height="18" viewBox="0 0 18 18" aria-label="Next slide">
  <circle cx="9" cy="9" r="9" fill="#111"/><path d="M7.5 5 L11.5 9 L7.5 13" stroke="#fff" stroke-width="2" fill="none"/>
</svg>

<h2 class="section-title" style="left:49px;top:580px;">We are high-end chefs that produce delicious, fresh and seasonal food</h2>
<div class="photo" style="left:49px;top:618px;width:248px;height:138px;background:linear-gradient(120deg,#7fa94a,#d6b778 50%,#b58a4a);" role="img" aria-label="Photograph of crispy spring rolls with salad and dipping sauce"></div>
<p class="abs intro-text">Hello, we’re Hannah and Tom, co-owners of Thistle Catering. We are a small, but perfectly formed team of Hartwell’s trained chefs passionate about top quality ingredients and good food. Based in West London, we offer bespoke catering services for corporate and private events. Whether you’re after cold finger food for a working lunch, a fine-dining experience for a group of close friends or creative and nutritious snacks for a children’s party, we can deliver a culinary experience that delights.</p>
<a class="btn abs" href="#" style="left:308px;top:784px;">More</a>

<div class="abs rule"></div>

<h2 class="section-title" style="left:51px;top:856px;">Our Services</h2>
<div class="photo" style="left:49px;top:887px;width:252px;height:161px;background:radial-gradient(ellipse at 45% 50%,#e2c29a 0%,#f3ebe0 45%,#e9e6e2 100%);" role="img" aria-label="Photograph of seared scallop with chives"></div>
<div class="column" style="left:49px;top:1066px;">
  <p class="column-text">Thistle offers a wide range of services, allowing the food to be tailored perfectly to your event. Click through our menu of options to the right for more information.<br><br>Can't see quite what you're looking for? We'd love to discuss catering requirements with you please <a href="#">get in touch</a></p>
</div>

<h2 class="section-title" style="left:335px;top:856px;">Seasonal Recipe</h2>
<div class="photo" style="left:335px;top:887px;width:252px;height:161px;background:linear-gradient(160deg,#c4122a 0%,#d83a4a 55%,#f1d9a8 100%);" role="img" aria-label="Photograph of redcurrants and raspberries on a dessert"></div>
<div class="column" style="left:336px;top:1066px;">
  <p class="column-text">We tailor our menus throughout the year to make the most of seasonally available ingredients. Click through our sample menus for ideas; these are just a few examples of canapes and dishes we can provide.</p>
  <a class="btn" href="#" style="margin-left:-1px;">More</a>
</div>

<aside>
  <div class="abs sidebar-box"></div>
  <div class="abs sidebar-title" style="left:685px;top:585px;">Menus</div>
  <div class="thumb" style="left:684px;top:619px;background:linear-gradient(135deg,#e8e0d0,#c9b08a);" role="img" aria-label="Canapé photograph"></div>
  <div class="thumb" style="left:770px;top:619px;background:linear-gradient(135deg,#c84a4a,#e8d0b0);" role="img" aria-label="Canapé photograph"></div>
  <div class="thumb" style="left:684px;top:705px;background:linear-gradient(135deg,#7aa04a,#e0c08a);" role="img" aria-label="Canapé photograph"></div>
  <div class="thumb" style="left:770px;top:705px;background:linear-gradient(135deg,#ece4d6,#b99a6a);" role="img" aria-label="Canapé photograph"></div>
  <div class="thumb" style="left:684px;top:791px;background:linear-gradient(135deg,#d04a8a,#3a2a3a);" role="img" aria-label="Canapé photograph"></div>
  <div class="thumb" style="left:770px;top:791px;background:linear-gradient(135deg,#e88aa0,#f0b030);" role="img" aria-label="Photograph of drinks in glasses"></div>
  <div class="abs see-all">See all</div>

  <div class="abs fb-avatar" role="img" aria-label="Page avatar photograph"></div>
  <div class="abs fb-name">Thistle Catering, London</div>
  <div class="abs fb-like">Like</div>
  <div class="abs fb-count">24</div>

  <div class="abs video-head"><span class="sidebar-title">Featured Video</span></div>
  <div class="abs video" role="img" aria-label="Video still of a miniature gardener mowing a surface of food"></div>
  <svg class="abs" style="left:660px;top:1168px;" width="204" height="26" viewBox="0 0 204 26" aria-label="Video controls">
    <rect x="0" y="0" width="36" height="26" rx="3" fill="#222"/>
    <path d="M14 7 L24 13 L14 19 Z" fill="#fff"/>
    <rect x="40" y="4" width="162" height="18" rx="3" fill="#333"/>
    <rect x="80" y="11" width="78" height="3" fill="#777"/>
    <text x="45" y="17" font-family="Arial, sans-serif" font-size="8" fill="#ddd">00:00</text>
  </svg>
  <svg class="abs" style="left:750px;top:1108px;" width="24" height="24" viewBox="0 0 24 24" aria-label="Play">
    <rect width="24" height="24" rx="3" fill="#222"/><path d="M9 6 L18 12 L9 18 Z" fill="#fff"/>
  </svg>
</aside>
</body>
</html>
```